Bi-Lingual Trash and Recycle Sign

Hello,

Pretty straight forward. I have not been able to find the exact sign we need for a property with trash and recycle guidelines. I've found close, but not complete. We are looking to have metal 12x18 street sign type signs made to provide these instructions. Attached is a sample taken from the web. I want to be sure to avoid conflicting with them so looking for the same wording but in our own. I'd also like to include our company logo, also attached in vector in horizontal and vertical for inclusion.

```html
<!DOCTYPE html>
<html lang="en">
<head>
<meta charset="utf-8">
<title>Recycle Sign – Halvern Management</title>
<link rel="stylesheet" href="https://fonts.googleapis.com/css2?family=Roboto+Slab:wght@600;700;800&family=Rubik:wght@700;800&display=swap">
<style>
  :root {
    --paper: #ffffff;
    --green: #0f9a4a;
    --bin-green: #249b45;
    --red: #c8282e;
    --maroon: #4a1628;
    --plum: #6b2a45;
    --accent-tint: #efe6ea;
    --bag-blue: #9fcfe6;
  }
  * { margin: 0; padding: 0; box-sizing: border-box; }
  html, body { width: 870px; height: 1200px; overflow: hidden; background: var(--paper); }
  .sign { position: relative; width: 870px; height: 1200px; background: var(--paper); overflow: hidden; }

  .accent-band { position: absolute; left: 767px; top: 110px; width: 103px; height: 895px; background: var(--accent-tint); }

  .brand { position: absolute; left: 0; width: 870px; top: 100px; display: flex; justify-content: center; align-items: center; gap: 14px; }
  .brand-square { width: 34px; height: 34px; background: var(--plum); }
  .brand-name { font-family: "Rubik", sans-serif; font-weight: 700; font-size: 42px; color: var(--maroon); letter-spacing: 1px; }

  .headline { position: absolute; left: 140px; width: 590px; top: 280px; text-align: center;
    font-family: "Roboto Slab", serif; font-weight: 800; font-size: 104px; line-height: 1; color: var(--green); letter-spacing: 3px; }

  .notice { position: absolute; top: 436px; width: 300px; text-align: center; }
  .notice-left { left: 106px; }
  .notice-right { left: 438px; }
  .no-row { display: flex; justify-content: center; align-items: center; gap: 8px; height: 90px; }
  .no-word { font-family: "Rubik", sans-serif; font-weight: 800; font-size: 116px; line-height: 1; color: var(--red); letter-spacing: -4px; }
  .no-symbol { width: 92px; height: 88px; }
  .notice-text { margin-top: 12px; font-family: "Rubik", sans-serif; font-weight: 700; font-size: 38px; line-height: 45px; color: var(--maroon); }

  .divider { position: absolute; left: 412px; top: 438px; width: 2px; height: 213px; background: var(--red); }

  .bin-artwork { position: absolute; left: 0; top: 711px; width: 422px; height: 489px; background: var(--bin-green); }

  .sort-label { position: absolute; left: 433px; top: 1032px; width: 384px; height: 116px; }
  .sort-frame { position: absolute; inset: 0; }
  .sort-text { position: absolute; left: 40px; top: 12px; width: 330px; text-align: center;
    font-family: "Roboto Slab", serif; font-weight: 700; font-size: 40px; line-height: 44px; letter-spacing: 1px; }
  .sort-text .line-top { color: var(--plum); display: block; }
  .sort-text .line-bottom { color: var(--green); display: block; letter-spacing: 2px; }
</style>
</head>
<body>
<main class="sign">
  <div class="accent-band"></div>

  <header class="brand">
    <span class="brand-square"></span>
    <span class="brand-name">HALVERN MANAGEMENT</span>
  </header>

  <h1 class="headline">RECYCLE</h1>

  <section class="notice notice-left" lang="en">
    <div class="no-row">
      <span class="no-word">N</span>
      <svg class="no-symbol" viewBox="0 0 100 100">
        <circle cx="50" cy="50" r="30" fill="var(--bag-blue)" role="img" aria-label="Plastic bag"/>
        <circle cx="50" cy="50" r="42" fill="none" stroke="var(--red)" stroke-width="14"/>
        <line x1="22" y1="22" x2="78" y2="78" stroke="var(--red)" stroke-width="13"/>
      </svg>
    </div>
    <p class="notice-text">PLASTIC<br>BAGS<br>ACCEPTED</p>
  </section>

  <div class="divider"></div>

  <section class="notice notice-right" lang="es">
    <div class="no-row">
      <span class="no-word">N</span>
      <svg class="no-symbol" viewBox="0 0 100 100">
        <circle cx="50" cy="50" r="30" fill="var(--bag-blue)" role="img" aria-label="Bolsa plástica"/>
        <circle cx="50" cy="50" r="42" fill="none" stroke="var(--red)" stroke-width="14"/>
        <line x1="22" y1="22" x2="78" y2="78" stroke="var(--red)" stroke-width="13"/>
      </svg>
    </div>
    <p class="notice-text">SE ACEPTAN<br>BOLSAS<br>PLÁSTICAS</p>
  </section>

  <div class="bin-artwork" role="img" aria-label="Illustration of a green recycling bin with lid and white recycling symbol"></div>

  <div class="sort-label">
    <svg class="sort-frame" viewBox="0 0 384 116" aria-hidden="true">
      <polygon points="17,1 383,1 383,115 1,115" fill="none" stroke="var(--green)" stroke-width="1.5"/>
    </svg>
    <p class="sort-text"><span class="line-top">SINGLE SORT</span><span class="line-bottom">RECYCLING</span></p>
  </div>
</main>
</body>
</html>
```